Cedarbend Ridge Footraces

We need a website (wordpress) design for a new website that we will be launching. This is for a new trail racing series in Canada.
We recently had a logo designed so want to incorporate the colours of the logo on the website design. Especially the dark blue, green and orange.
Websites that we like for comparison of trail running race themes are:
https://www.mossyboulderrunning.example/
https://www.quillpathcircuit.example/
http://www.tidecovecircuit.example/
https://www.amberfellcircuit.example/
http://www.brookmarchrunseries.example/

Target Market(s)

Outdoor trail runners

Coding

Coded - Design and coding required

Number of Pages Required

4 page

Font styles to use
Sans Serif

Colors
0255a3
33b8a4
f37122

Requirements
Must have
• There will be a main page with eye catching design noting what we do. Page 2 and 3 will be for each race in the series. Page 1 will be a specific race, and page 2 with be for another race. page 3 and 4 will be for future races that we add so that each race has their own page.
• Our races all take place in the mountains, so using graphics including mountains, rivers, trees is all a requirement for us.
• Our logo is attached, we want to use the colours of the logo in the website design.
Nice to have
• Outdoor theme is a nice to have. We like wood and earth tone colours, and pictures/graphics of runners and mountains and trees.
• There are 4 people involved in our organization. We'd like a photo and brief blurb of each of us, similar to how this website did their layout: https://www.mossyboulderrunning.example/

```html
<!DOCTYPE html>
<html lang="en">
<head>
<meta charset="utf-8">
<title>Cedarbend Ridge Footraces</title>
<link href="https://fonts.googleapis.com/css2?family=Arvo:wght@400;700&family=Bevan&family=Roboto+Condensed:wght@700&family=Cormorant+Garamond:wght@400&display=swap" rel="stylesheet">
<style>
  :root {
    --orange: #f37122;
    --blue: #0a6399;
    --green: #33cc99;
    --races-bg: #464646;
    --blogs-bg: #2a2a2a;
    --story-bg: #06231f;
    --white: #ffffff;
  }
  * { margin: 0; padding: 0; box-sizing: border-box; }
  html, body { width: 1200px; height: 1200px; overflow: hidden; }
  body { position: relative; background: var(--story-bg); font-family: "Arvo", serif; color: var(--white); }

  /* Hero */
  .hero { position: absolute; left: 0; top: 0; width: 1200px; height: 220px; overflow: hidden; }
  .hero-photo { position: absolute; inset: 0;
    background: radial-gradient(ellipse at 60% 70%, #6e5a4a 0%, #3e3a30 40%, #1e261c 75%, #141a14 100%); }
  .brand { position: absolute; left: 148px; top: 4px; display: flex; align-items: center; gap: 6px; }
  .brand-mark { width: 18px; height: 18px; border-radius: 50%; background: var(--orange); }
  .brand-name { font-family: "Arvo", serif; font-weight: 700; font-size: 11px; line-height: 12px; color: var(--white); width: 80px; text-transform: uppercase; }
  .main-nav { position: absolute; left: 322px; top: 15px; font-family: "Arvo", serif; font-weight: 700; font-size: 10px; color: var(--orange); }
  .main-nav a { color: var(--orange); text-decoration: none; }
  .main-nav span { margin: 0 4px; }
  .account { position: absolute; left: 912px; top: 4px; display: flex; align-items: center; gap: 16px; }
  .account a { color: var(--orange); font-weight: 700; font-size: 10px; text-decoration: none; }
  .hero-title { position: absolute; left: 153px; top: 66px; font-family: "Bevan", serif; font-size: 28px; color: var(--orange); }
  .hero-text { position: absolute; left: 156px; top: 102px; width: 232px; font-weight: 700; font-size: 10.5px; line-height: 13.6px; }
  .ticket-btn { position: absolute; left: 486px; top: 151px; width: 166px; height: 40px; background: var(--orange); color: var(--white);
    font-weight: 700; font-size: 15px; display: flex; align-items: center; justify-content: center; }

  /* Races */
  .races { position: absolute; left: 0; top: 220px; width: 1200px; height: 340px; background: var(--races-bg); }
  .section-title { font-family: "Bevan", serif; text-align: center; font-size: 27px; }
  .races .section-title { position: absolute; top: 0; width: 100%; line-height: 32px; }
  .race-grid { position: absolute; left: 150px; top: 37px; width: 900px; height: 303px; display: flex; }
  .race-card { width: 225px; height: 303px; position: relative; }
  .race-card.blue { background: var(--blue); }
  .race-card.green { background: var(--green); }
  .race-photo { height: 138px; }
  .race-photo.p1 { background: linear-gradient(180deg, #c9d8e6 0%, #9fb69a 55%, #8c8470 100%); }
  .race-photo.p2 { background: linear-gradient(180deg, #6d7f88 0%, #4d5a5e 50%, #6d6a62 100%); }
  .race-photo.p3 { background: linear-gradient(180deg, #8fb3cf 0%, #b5a58a 65%, #8c7a5e 100%); }
  .race-photo.p4 { background: linear-gradient(180deg, #2e3f40 0%, #3f4b4a 60%, #5a5e58 100%); }
  .race-date { text-align: center; font-weight: 700; font-size: 15px; margin-top: 5px; }
  .race-text { padding: 0 9px; font-size: 9.6px; line-height: 13px; margin-top: 4px; letter-spacing: 0.2px; }
  .race-btn { position: absolute; left: 37px; bottom: 14px; width: 151px; height: 29px; border-radius: 15px; background: var(--orange);
    font-weight: 700; font-size: 9.5px; display: flex; align-items: center; justify-content: center; }

  /* Blogs */
  .blogs { position: absolute; left: 0; top: 560px; width: 1200px; height: 243px; background: var(--blogs-bg); }
  .blog-photo { position: absolute; left: 150px; top: 0; width: 397px; height: 243px;
    background: linear-gradient(180deg, #6d7d74 0%, #2f4a42 45%, #1d3a34 75%, #27463f 100%); }
  .blogs .section-title { position: absolute; left: 600px; width: 420px; top: 0; font-size: 28px; line-height: 32px; }
  .blog-text { position: absolute; left: 600px; top: 33px; width: 446px; font-family: "Roboto Condensed", sans-serif; font-weight: 700;
    font-size: 12.4px; line-height: 13.6px; letter-spacing: -0.4px; }
  .subscribe-btn { position: absolute; left: 651px; top: 193px; width: 165px; height: 43px; background: var(--orange);
    font-weight: 700; font-size: 14px; display: flex; align-items: center; justify-content: center; }

  /* Story */
  .story { position: absolute; left: 0; top: 803px; width: 1200px; height: 227px; background: var(--story-bg); }
  .story .section-title { position: absolute; top: 0; width: 100%; font-size: 27px; line-height: 34px; }
  .team-member { position: absolute; top: 35px; width: 151px; height: 178px; }
  .avatar { position: absolute; left: 28px; top: 0; width: 94px; height: 66px; border-radius: 50% 50% 0 0 / 100% 100% 0 0;
    background: radial-gradient(circle at 50% 60%, #c4987c 0%, #6e4a3a 55%, #2a2420 100%); z-index: 2; }
  .avatar.alt { background: radial-gradient(circle at 50% 60%, #e1bca8 0%, #b0684a 55%, #6d7a80 100%); }
  .member-card { position: absolute; left: 0; top: 58px; width: 151px; height: 120px; padding: 10px 8px 0 17px; }
  .member-card.green { background: var(--green); }
  .member-card.blue { background: var(--blue); }
  .member-bio { font-weight: 700; font-size: 5.6px; line-height: 8.2px; }
  .member-name { text-align: center; font-family: "Bevan", serif; font-size: 13px; line-height: 11px; margin-top: 2px; letter-spacing: 1px; }
  .member-role { text-align: center; font-weight: 700; font-size: 10px; letter-spacing: 0.8px; margin-top: 1px; }

  /* Footer */
  .site-footer { position: absolute; left: 0; top: 1030px; width: 1200px; height: 170px; overflow: hidden; }
  .track-photo { position: absolute; inset: 0; background: linear-gradient(180deg, #8a2e22 0%, #a33a2a 50%, #8f3022 100%); }
  .lane { position: absolute; left: 0; width: 1200px; height: 2px; background: rgba(255,255,255,0.55); }
  .volunteer { position: absolute; left: 151px; top: 16px; width: 330px; }
  .volunteer h3 { font-family: "Arvo", serif; font-weight: 700; font-size: 15px; line-height: 16px; letter-spacing: 0.4px; }
  .volunteer p { font-family: "Arvo", serif; font-size: 14.5px; line-height: 13.8px; letter-spacing: 0.6px; }
  .community { position: absolute; left: 603px; top: 35px; font-family: "Cormorant Garamond", serif; font-size: 19px; line-height: 21px; }
  .community .caps { text-transform: uppercase; }
  .signup { position: absolute; left: 517px; top: 80px; width: 360px; height: 14px; display: flex; }
  .signup-input { flex: 1; background: var(--white); border-radius: 7px 0 0 7px; color: #b8b8b8;
    font-family: "Cormorant Garamond", serif; font-size: 11px; padding-left: 72px; line-height: 14px; }
  .signup-btn { width: 98px; background: var(--orange); border-radius: 0 7px 7px 0; font-family: "Cormorant Garamond", serif; font-size: 12px; text-align: center; line-height: 14px; }
  .social { position: absolute; left: 883px; top: 34px; display: flex; gap: 14px; }
  .social span { width: 26px; height: 16px; border: 2px solid var(--white); border-radius: 4px; display: block; }
  .legal { position: absolute; left: 0; top: 149px; width: 100%; text-align: center; font-family: "Cormorant Garamond", serif; font-size: 21px; }
</style>
</head>
<body>

<header class="hero">
  <div class="hero-photo" role="img" aria-label="Trail runner with poles on a rocky forest path"></div>
  <div class="brand">
    <span class="brand-mark"></span>
    <span class="brand-name">Cedarbend Ridge Footraces</span>
  </div>
  <nav class="main-nav">
    <a href="#">HOME</a><span>|</span><a href="#">Events</a><span>|</span><a href="#">PHOTOS</a><span>|</span><a href="#">RESULTS</a><span>|</span><a href="#">BLOG</a>
  </nav>
  <div class="account">
    <svg width="40" height="28" viewBox="0 0 40 28" aria-hidden="true">
      <circle cx="20" cy="14" r="13" fill="none" stroke="#1a1a1a" stroke-width="1.5"/>
      <circle cx="20" cy="11" r="5" fill="none" stroke="#1a1a1a" stroke-width="1.5"/>
      <path d="M10 23c3-5 17-5 20 0" fill="none" stroke="#1a1a1a" stroke-width="1.5"/>
    </svg>
    <a href="#">Login</a>
  </div>
  <h1 class="hero-title">Happy Trail</h1>
  <p class="hero-text">Lorem ipsum dolor sit amet, consectetur adipisicing elit, sed do eiusmod tempor incididunt ut labore et dolore magna aliqua. Ut enim ad minim veniam, quis nostrud exercitation ullamco laboris nisi ut aliquip ex ea commodo consequat. Duis aute</p>
  <a class="ticket-btn">Buy A Ticket</a>
</header>

<section class="races">
  <h2 class="section-title">Races</h2>
  <div class="race-grid">
    <article class="race-card blue">
      <div class="race-photo p1" role="img" aria-label="Runner on a gravel path beside a field"></div>
      <h3 class="race-date">August 13, 2018</h3>
      <p class="race-text">Lorem ipsum dolor sit amet, consectetur adipisicing elit, sed do eiusmod tempor incididunt ut labore et dolore magna aliqua. Ut enim ad minim veniam, quis nostrud exercitation ullamco laboris nisi ut aliquip ex ea commodo consequat.</p>
      <a class="race-btn">Check Out This Race</a>
    </article>
    <article class="race-card green">
      <div class="race-photo p2" role="img" aria-label="Crowd of runners on a road race"></div>
      <h3 class="race-date">August 13, 2018</h3>
      <p class="race-text">Lorem ipsum dolor sit amet, consectetur adipisicing elit, sed do eiusmod tempor incididunt ut labore et dolore magna aliqua. Ut enim ad minim veniam, quis nostrud exercitation ullamco laboris nisi ut aliquip ex ea commodo consequat.</p>
      <a class="race-btn">Check Out This Race</a>
    </article>
    <article class="race-card blue">
      <div class="race-photo p3" role="img" aria-label="Runner in a jacket on open grassland"></div>
      <h3 class="race-date">August 13, 2018</h3>
      <p class="race-text">Lorem ipsum dolor sit amet, consectetur adipisicing elit, sed do eiusmod tempor incididunt ut labore et dolore magna aliqua. Ut enim ad minim veniam, quis nostrud exercitation ullamco laboris nisi ut aliquip ex ea commodo consequat.</p>
      <a class="race-btn">Check Out This Race</a>
    </article>
    <article class="race-card green">
      <div class="race-photo p4" role="img" aria-label="Runner in a cap on a lakeside path"></div>
      <h3 class="race-date">August 13, 2018</h3>
      <p class="race-text">Lorem ipsum dolor sit amet, consectetur adipisicing elit, sed do eiusmod tempor incididunt ut labore et dolore magna aliqua. Ut enim ad minim veniam, quis nostrud exercitation ullamco laboris nisi ut aliquip ex ea commodo consequat.</p>
      <a class="race-btn">Check Out This Race</a>
    </article>
  </div>
</section>

<section class="blogs">
  <div class="blog-photo" role="img" aria-label="Misty evergreen forest reflected in a mountain lake"></div>
  <h2 class="section-title">Our Blogs</h2>
  <p class="blog-text">Lorem ipsum dolor sit amet, consectetur adipisicing elit, sed do eiusmod tempor incididunt ut labore et dolore magna aliqua. Ut enim ad minim veniam, quis nostrud exercitation ullamco laboris nisi ut aliquip ex ea commodo consequat. Duis aute irure dolor in reprehenderit in voluptate velit esse cillum dolore eu fugiat nulla pariatur. Excepteur sint occaecat cupidatat non proident, sunt in culpa qui officia deserunt mollit anim id est laborum. Sed ut perspiciatis unde omnis iste natus error sit voluptatem accusantium doloremque laudantium, totam rem aperiam, eaque ipsa quae ab illo inventore veritatis et quasi architecto beatae vitae dicta sunt explicabo. Nemo enim ipsam voluptatem quia voluptas sit aspernatur aut odit aut fugit, sed quia consequuntur magni dolores eos qui ratione voluptatem sequi nesciunt. Neque porro quisquam est, qui dolorem ipsum quia dolor sit amet, consectetur, adipisci velit, sed quia non numquam eius modi tempora incidunt ut labore et dolore magnam aliquam quaerat voluptatem.</p>
  <a class="subscribe-btn">Subscribe</a>
</section>

<section class="story">
  <h2 class="section-title">Our Story</h2>
  <div class="team-member" style="left:151px">
    <div class="avatar" role="img" aria-label="Portrait of team member"></div>
    <div class="member-card green">
      <p class="member-bio">Rowan has mapped mountain routes for a decade, marking every switchback by hand. He loves early starts, cold creeks and cheering the final runner across the line at every event.</p>
      <p class="member-name">Rowan<br>Pellfield</p>
      <p class="member-role">Race Director</p>
    </div>
  </div>
  <div class="team-member" style="left:400px">
    <div class="avatar alt" role="img" aria-label="Portrait of team member"></div>
    <div class="member-card blue">
      <p class="member-bio">Rowan has mapped mountain routes for a decade, marking every switchback by hand. He loves early starts, cold creeks and cheering the final runner across the line at every event.</p>
      <p class="member-name">Rowan<br>Pellfield</p>
      <p class="member-role">Race Director</p>
    </div>
  </div>
  <div class="team-member" style="left:650px">
    <div class="avatar" role="img" aria-label="Portrait of team member"></div>
    <div class="member-card green">
      <p class="member-bio">Rowan has mapped mountain routes for a decade, marking every switchback by hand. He loves early starts, cold creeks and cheering the final runner across the line at every event.</p>
      <p class="member-name">Rowan<br>Pellfield</p>
      <p class="member-role">Race Director</p>
    </div>
  </div>
  <div class="team-member" style="left:899px">
    <div class="avatar" role="img" aria-label="Portrait of team member"></div>
    <div class="member-card blue">
      <p class="member-bio">Rowan has mapped mountain routes for a decade, marking every switchback by hand. He loves early starts, cold creeks and cheering the final runner across the line at every event.</p>
      <p class="member-name">Rowan<br>Pellfield</p>
      <p class="member-role">Race Director</p>
    </div>
  </div>
</section>

<footer class="site-footer">
  <div class="track-photo" role="img" aria-label="Red running track with white lane lines"></div>
  <div class="lane" style="top:12px"></div>
  <div class="lane" style="top:126px"></div>
  <div class="volunteer">
    <h3>VOLUNTEER FOR OUR RACES</h3>
    <p>We love our volunteers. The races would not run without you. Hit that button to chat with us about volunteering at any of our upcoming races.</p>
  </div>
  <div class="community">
    <p>Want the inside scoop?</p>
    <p class="caps">Join the community</p>
  </div>
  <div class="signup">
    <div class="signup-input">Type Your Email Here</div>
    <div class="signup-btn">Join</div>
  </div>
  <div class="social" aria-label="Social links">
    <span></span><span></span><span></span>
  </div>
  <p class="legal">Privacy - Terms Of Use - Ad Preferences</p>
</footer>

</body>
</html>
```